依頼詳細
入れて貰いたいワードです。

焼餃子の画像は用意お願いします。

・餃子の街 宇都宮
・栃木県宇都宮市出身のオーナーの一押し
・白峰の冷凍生餃子
・特製みそだれで旨い
・宇都宮の餃子として28年 多くの方に愛され栃木県内のラーメン店や飲食店でも多く利用されています

【商品】

・白峰の冷凍生餃子 20個入り 680円
・お徳用 白峰の冷凍生餃子 50個入り 1580円

*上記2品、餃子のたれ&特製味噌だれ付

記載項目
【販売店舗】
サニーステップキックボクシング&ジム
北九州市小倉北区旭町2丁目5-3-2F
093-514-2086
営業時間 10~13時 17~20時
*営業時間外に購入ご希望の方は営業時間内にお電話下さいませ。
サイズ
A4
ページ数
片面
希望イメージ
シンプル 複雑
単色 カラフル
暗い 明るい
日常 高級
遊び心 厳粛
未来的 伝統的
女性的 男性的
希望する色
赤系、黄・オレンジ系
納品ファイル
• 高解像度JPG (.jpg)
• イラストレーター形式 (.ai)
依頼詳細

・特製みそだれで旨い ⇒ 包み名人 味噌だれで旨い

に変更お願いします
*画像も添付します

```html
<!DOCTYPE html>
<html lang="ja">
<head>
<meta charset="utf-8">
<title>白峰の冷凍生餃子</title>
<link rel="stylesheet" href="https://fonts.googleapis.com/css2?family=Noto+Sans+JP:wght@400;700;900&family=Noto+Serif+JP:wght@700;900&family=Yuji+Syuku&display=swap">
<style>
:root{
  --red:#d8261c;
  --deep-red:#b3140f;
  --cream:#fff6ea;
  --ink:#2b1a12;
  --white:#ffffff;
  --yellow:#ffe14a;
}
*{margin:0;padding:0;box-sizing:border-box}
html,body{width:848px;height:1200px;overflow:hidden;background:var(--white)}
.flyer{position:relative;width:848px;height:1200px;overflow:hidden;background:var(--cream);font-family:"Noto Sans JP",sans-serif;color:var(--ink)}
.product-photo{position:absolute;left:0;top:0;width:848px;height:370px;background:
  radial-gradient(ellipse 200px 150px at 160px 220px,#f4efe6 0%,#e8ddd0 60%,rgba(232,221,208,0) 100%),
  radial-gradient(ellipse 260px 160px at 640px 220px,#f1ebe2 0%,#ded2c3 60%,rgba(222,210,195,0) 100%),
  radial-gradient(ellipse 70px 120px at 370px 200px,#e9773a 0%,rgba(233,119,58,0) 100%),
  linear-gradient(180deg,#f6b46a 0%,#f09a45 100%)}
.gyoza-photo{position:absolute;left:0;top:360px;width:848px;height:620px;background:
  radial-gradient(ellipse 380px 200px at 330px 330px,#f3d3a0 0%,#d99a52 45%,rgba(190,120,60,0) 100%),
  radial-gradient(ellipse 160px 120px at 90px 470px,#f4c64e 0%,rgba(244,198,78,0) 100%),
  linear-gradient(165deg,#c98a4a 0%,#b06a2e 45%,#e6b883 80%,#fbe9d2 100%)}
.photo-fade{position:absolute;left:0;top:820px;width:848px;height:380px;background:linear-gradient(180deg,rgba(255,246,234,0) 0%,rgba(255,246,234,.9) 35%,var(--cream) 60%)}
.headline-tag{position:absolute;left:113px;top:40px;padding:4px 22px;background:var(--red);color:var(--white);font-weight:700;font-size:30px;border-radius:6px;letter-spacing:1px;white-space:nowrap}
.product-name{position:absolute;left:127px;top:96px;font-family:"Noto Serif JP",serif;font-weight:900;font-size:52px;color:var(--ink);letter-spacing:2px;white-space:nowrap;text-shadow:0 0 6px var(--white),0 0 3px var(--white)}
.price{position:absolute;top:205px;text-align:center;font-family:"Noto Serif JP",serif;font-weight:900;color:var(--red);line-height:1.2;text-shadow:0 0 5px var(--white),0 0 3px var(--white);white-space:nowrap}
.price .count{font-size:38px;display:block}
.price .yen{font-size:40px;display:block}
.price-small{left:118px}
.price-large{left:470px}
.value-badge{position:absolute;left:386px;top:228px;width:72px;height:72px;border-radius:50%;background:var(--yellow);color:var(--red);font-weight:900;font-size:20px;display:flex;align-items:center;justify-content:center}
.ribbon{position:absolute;left:0;padding:6px 40px 6px 34px;background:var(--red);color:var(--white);font-weight:700;font-size:26px;white-space:nowrap;clip-path:polygon(0 0,100% 0,93% 50%,100% 100%,0 100%)}
.ribbon-owner{top:428px}
.ribbon-sauce{top:492px}
.city-line{position:absolute;writing-mode:vertical-rl;font-family:"Noto Serif JP",serif;font-weight:900;font-size:40px;color:var(--ink);line-height:1;white-space:nowrap;text-shadow:0 0 6px var(--white),0 0 3px var(--white)}
.city-left{left:505px;top:400px}
.city-right{left:772px;top:470px}
.big-char{position:absolute;font-family:"Yuji Syuku",serif;line-height:1;color:var(--red);text-shadow:0 0 10px rgba(255,255,255,.7)}
.big-gyo{left:548px;top:445px;font-size:215px}
.big-ko{left:560px;top:695px;font-size:240px}
.story{position:absolute;left:150px;top:915px;width:400px;text-align:center;font-size:18px;font-weight:700;line-height:1.6;color:var(--ink)}
.shop-label{position:absolute;left:14px;top:1028px;padding:3px 12px;background:var(--red);color:var(--white);font-weight:700;font-size:22px}
.shop-info{position:absolute;left:24px;top:1072px;font-size:16px;line-height:1.55;color:var(--ink);white-space:nowrap}
.shop-info .hours{font-weight:700;font-size:21px}
.note{position:absolute;left:24px;top:1172px;font-size:12px;color:var(--ink);white-space:nowrap}
.phone{position:absolute;left:488px;top:1086px;display:flex;align-items:center;gap:10px;font-weight:700;font-size:36px;color:var(--ink);white-space:nowrap}
.phone svg{width:38px;height:38px;flex:none}
</style>
</head>
<body>
<main class="flyer">
  <div class="product-photo" role="img" aria-label="包装された冷凍生餃子の商品写真（20個入りと50個入り、たれの小袋）"></div>
  <div class="gyoza-photo" role="img" aria-label="皿に盛られた焼餃子とビールの写真"></div>
  <div class="photo-fade"></div>

  <div class="headline-tag">餃子のたれ＆特製味噌だれ付</div>
  <h1 class="product-name">白峰の冷凍生餃子</h1>

  <div class="price price-small"><span class="count">20個入り</span><span class="yen">680円</span></div>
  <div class="value-badge">お徳用</div>
  <div class="price price-large"><span class="count">50個入り</span><span class="yen">1580円</span></div>

  <div class="ribbon ribbon-owner">栃木県宇都宮市出身のオーナーの一押し</div>
  <div class="ribbon ribbon-sauce">包み名人 味噌だれで旨い</div>

  <div class="city-line city-left">「餃子の街」</div>
  <div class="city-line city-right">宇都宮の</div>
  <div class="big-char big-gyo">餃</div>
  <div class="big-char big-ko">子</div>

  <p class="story">宇都宮の餃子として28年<br>多くの方に愛され、栃木県内のラーメン店や<br>飲食店でも多く利用されています</p>

  <div class="shop-label">【販売店舗】</div>
  <div class="shop-info">
    サニーステップキックボクシング&amp;ジム<br>
    北九州市小倉北区旭町2丁目5-3-2F<br>
    <span class="hours">営業時間 10～13時　17～20時</span>
  </div>
  <p class="note">＊営業時間外に購入ご希望の方は営業時間内にお電話下さいませ。</p>

  <div class="phone">
    <svg viewBox="0 0 40 40" aria-hidden="true"><circle cx="20" cy="20" r="18" fill="none" stroke="#2b1a12" stroke-width="3"/><path d="M13 11c2-1 3 0 4 2l1 3c0 1-1 2-2 3 1 3 3 5 6 6 1-1 2-2 3-2l3 1c2 1 3 2 2 4-1 2-3 3-5 2-6-2-11-7-13-13-1-2 0-5 1-6z" fill="#2b1a12"/></svg>
    <span>093-514-2086</span>
  </div>
</main>
</body>
</html>
```